Professional and creatice Life Coach - Business Card design

I just relaunched my website and now i a need a correspoonding business card for my task as life coach. My website is www.tbalrond.com as reference. The compass is kind of a symbol for my work, as I help people navigate through their challenging phases in life. The business card should be colorful, but not too playful as I also adress business people. So it sould be creative, but professional (also to suport my other business as Management Consultant)

Target Market(s)

People who want to get teir problems resolved, in business, partnership and other personal realms

Industry/Entity Type

Life Coaching

Contact Information for Business Card

Front side should include Name, Phone number, Email, Website and address

Font styles to use
Sans Serif

Colors
add136

Requirements
Must have
• "Mag. Leopold Brantner" -> Name
"Energetische Praxis" -> Jobtitle (describing my profession as life coach)
colours and style should match my website www.tbalrond.com
Nice to have
• a compass as a symbol

```html
<!DOCTYPE html>
<html lang="de">
<head>
<meta charset="utf-8">
<title>Leopold Brantner – Visitenkarte</title>
<link rel="stylesheet" href="https://fonts.googleapis.com/css2?family=Mulish:wght@400;600;800&display=swap">
<style>
  :root {
    --lime: #add136;
    --lime-deep: #9cbf2c;
    --ink: #2b2b2b;
    --grey: #555555;
    --rule: #c9c9c9;
    --paper: #ffffff;
    --stage: #2f2f2f;
    --faint: #f0f0f0;
  }
  * { margin: 0; padding: 0; box-sizing: border-box; }
  html, body { width: 1200px; height: 866px; overflow: hidden; }
  body {
    background: var(--stage);
    font-family: "Mulish", "Century Gothic", sans-serif;
    display: flex; flex-direction: column; align-items: center; justify-content: center;
    gap: 48px;
  }
  .card {
    position: relative;
    width: 580px; height: 374px;
    overflow: hidden;
    box-shadow: 0 10px 24px rgba(0,0,0,.45);
  }

  /* Front */
  .card--front { background: var(--paper); }
  .front__halo {
    position: absolute; left: 40px; top: -30px;
    width: 240px; height: 240px; border-radius: 50%;
    border: 26px solid var(--faint);
  }
  .front__band {
    position: absolute; left: 0; bottom: 0;
    width: 200px; height: 8px; background: var(--lime);
  }
  .contact { position: absolute; left: 38px; top: 104px; }
  .contact__name { color: var(--lime); font-weight: 800; font-size: 19px; letter-spacing: .3px; }
  .contact__role { color: var(--grey); font-size: 15px; margin: 2px 0 10px; }
  .contact__list { list-style: none; color: var(--ink); font-size: 14px; line-height: 21px; }
  .contact__list li { display: flex; align-items: center; gap: 8px; }
  .contact__list svg { width: 12px; height: 12px; fill: var(--lime); flex: none; }
  .front__rule {
    position: absolute; left: 210px; right: 40px; top: 262px;
    height: 1px; background: var(--rule);
  }
  .brand {
    position: absolute; right: 40px; top: 200px;
    display: flex; align-items: center; gap: 12px;
  }
  .brand__dot { width: 34px; height: 34px; border-radius: 50%; background: var(--lime); }
  .brand__name { color: var(--ink); font-weight: 800; font-size: 26px; letter-spacing: .5px; }
  .address {
    position: absolute; right: 40px; bottom: 38px;
    text-align: right; color: var(--ink); font-size: 14px; line-height: 19px;
  }

  /* Back */
  .card--back { background: var(--lime); display: flex; align-items: center; justify-content: center; }
  .back__halo {
    position: absolute; left: 50%; top: 50%;
    width: 250px; height: 250px; margin: -125px 0 0 -125px;
    border-radius: 50%; border: 22px solid var(--lime-deep);
  }
  .back__name { position: relative; color: var(--ink); font-weight: 800; font-size: 42px; letter-spacing: .5px; }
</style>
</head>
<body>
  <section class="card card--front" aria-label="Vorderseite">
    <div class="front__halo"></div>
    <div class="contact">
      <p class="contact__name">Mag. Leopold Brantner</p>
      <p class="contact__role">Energetische Praxis</p>
      <ul class="contact__list">
        <li><svg viewBox="0 0 24 24"><path d="M6.6 10.8a15 15 0 0 0 6.6 6.6l2.2-2.2c.3-.3.7-.4 1-.2 1.1.4 2.3.6 3.6.6.6 0 1 .4 1 1V20c0 .6-.4 1-1 1A17 17 0 0 1 3 4c0-.6.4-1 1-1h3.5c.6 0 1 .4 1 1 0 1.3.2 2.5.6 3.6.1.3 0 .7-.2 1z"/></svg>+43 664 5550182</li>
        <li><svg viewBox="0 0 24 24"><path d="M2 5h20v14H2zm2 2v.5l8 5 8-5V7z"/></svg>leopold@brantner.one</li>
        <li><svg viewBox="0 0 24 24"><circle cx="12" cy="12" r="10"/></svg>www.tbalrond.com</li>
      </ul>
    </div>
    <div class="brand">
      <span class="brand__dot"></span>
      <span class="brand__name">Leopold Brantner</span>
    </div>
    <div class="front__rule"></div>
    <p class="address">Lindenweg 12, 5020 Salzburg<br>Österreich</p>
    <div class="front__band"></div>
  </section>

  <section class="card card--back" aria-label="Rückseite">
    <div class="back__halo"></div>
    <p class="back__name">Leopold Brantner</p>
  </section>
</body>
</html>
```